Design Website for Data Entry

Design a single webpage website with three tabs, or section for. See the attached PDF for info. This webpage is a data entry dadshboard.

Target Market(s)

N/A

Number of Pages Required

3 page

Colors

Designer to choose colors to be used in the design.

```html
<!DOCTYPE html>
<html lang="en">
<head>
<meta charset="utf-8">
<title>FILEHARBOR – File Upload</title>
<link href="https://fonts.googleapis.com/css2?family=Montserrat:wght@400;500;600;700&display=swap" rel="stylesheet">
<style>
:root{
  --header-bg:#0b1c26;
  --main-bg:#0f2633;
  --row-dark:#0a1921;
  --line:#1d3c4b;
  --field-border:#25475a;
  --field-icon-bg:#1e4456;
  --orange:#f47b20;
  --white:#ffffff;
  --muted:#7f97a3;
  --placeholder:#8aa3b0;
  --ok:#2fc43a;
  --bad:#e0242b;
}
*{box-sizing:border-box;margin:0;padding:0}
html,body{width:1200px;height:1078px;overflow:hidden}
body{background:var(--main-bg);font-family:'Montserrat',sans-serif;color:var(--white)}
.site-header{height:98px;background:var(--header-bg);border-bottom:1px solid var(--line);display:flex;align-items:center;justify-content:center}
.brand-name{font-size:32px;font-weight:700;color:var(--white);letter-spacing:.5px}
.upload{height:455px;padding-top:46px}
.upload-title{text-align:center;font-size:21px;font-weight:600;letter-spacing:.3px}
.upload-title .accent{color:var(--orange)}
.upload-form{width:652px;margin:33px auto 0;display:grid;grid-template-columns:1fr 1fr;gap:19px 19px}
.field{height:47px;border:1px solid var(--field-border);border-radius:3px;display:flex;align-items:stretch;overflow:hidden}
.field.wide{grid-column:1/3;height:157px}
.field-icon{width:45px;background:var(--field-icon-bg);display:flex;justify-content:center;align-items:center;flex-shrink:0}
.field.wide .field-icon{align-items:flex-start;padding-top:14px}
.field-label{flex:1;padding:0 18px;display:flex;align-items:center;font-size:15px;font-weight:500;color:var(--placeholder)}
.field.wide .field-label{align-items:flex-start;padding-top:14px}
.field-clip{width:44px;display:flex;align-items:center;justify-content:center}
.submit{height:47px;border:none;border-radius:3px;background:var(--orange);color:var(--white);font-family:inherit;font-size:15px;font-weight:600;letter-spacing:.5px;box-shadow:0 4px 10px rgba(0,0,0,.25)}
.file-list{list-style:none;border-top:1px solid var(--line)}
.file-row{height:111px;border-bottom:1px solid var(--line);background:var(--row-dark);display:flex;align-items:center;padding:0 127px}
.file-row:first-child{background:var(--main-bg)}
.file-thumb{width:74px;height:74px;border-radius:50%;flex-shrink:0}
.file-text{margin-left:20px;flex:1}
.file-name{font-size:17px;font-weight:500;margin-bottom:5px}
.file-desc{font-size:13.6px;line-height:22px;color:var(--muted);white-space:nowrap}
.status{width:24px;height:24px}
.site-footer{text-align:center;padding-top:31px;font-size:14px;color:var(--muted)}
</style>
</head>
<body>
<header class="site-header">
  <span class="brand-name">FILEHARBOR</span>
</header>

<main class="upload">
  <h1 class="upload-title"><span class="accent">FILE</span> UPLOAD</h1>
  <form class="upload-form">
    <div class="field">
      <span class="field-icon"><svg width="18" height="22" viewBox="0 0 18 22" fill="none" stroke="#c9d6dc" stroke-width="1.3"><path d="M1 1h11l5 5v15H1z"/><path d="M12 1v5h5M4 10h10M4 13h10M4 16h10"/></svg></span>
      <span class="field-label">File Name</span>
    </div>
    <div class="field">
      <span class="field-icon"><svg width="24" height="14" viewBox="0 0 24 14" fill="none" stroke="#c9d6dc" stroke-width="1.4"><path d="M1 7C5 1 19 1 23 7C19 13 5 13 1 7z"/><circle cx="12" cy="7" r="3"/></svg></span>
      <span class="field-label">File Icon</span>
      <span class="field-clip"><svg width="18" height="22" viewBox="0 0 18 22" fill="none" stroke="#7f97a3" stroke-width="1.4"><path d="M14 9l-7 7a3 3 0 0 1-4-4l8-8a2 2 0 0 1 3 3l-8 8"/></svg></span>
    </div>
    <div class="field wide">
      <span class="field-icon"><svg width="20" height="20" viewBox="0 0 20 20" fill="none" stroke="#c9d6dc" stroke-width="1.4"><path d="M2 18l1-5L14 2l4 4L7 17z"/><path d="M12 4l4 4M3 13l4 4"/></svg></span>
      <span class="field-label">File Description</span>
    </div>
    <div class="field">
      <span class="field-icon"><svg width="18" height="22" viewBox="0 0 18 22" fill="none" stroke="#c9d6dc" stroke-width="1.3"><path d="M1 1h11l5 5v15H1z"/><path d="M12 1v5h5M4 10h10M4 13h10M4 16h10"/></svg></span>
      <span class="field-label">Upload File</span>
      <span class="field-clip"><svg width="18" height="22" viewBox="0 0 18 22" fill="none" stroke="#7f97a3" stroke-width="1.4"><path d="M14 9l-7 7a3 3 0 0 1-4-4l8-8a2 2 0 0 1 3 3l-8 8"/></svg></span>
    </div>
    <button type="button" class="submit">SUBMIT</button>
  </form>
</main>

<ul class="file-list">
  <li class="file-row">
    <div class="file-thumb" role="img" aria-label="Orbit app icon" style="background:radial-gradient(circle,#3fb6e6 0 22%,#ffffff 24%)"></div>
    <div class="file-text"><h2 class="file-name">Orbit 17.6</h2><p class="file-desc">Lorem ipsum dolor sit amet, consectetur adipiscing elit. Aliquam ut dignissim dolor.<br>Pellentesque ex elit, interdum at ex nec, tincidunt faucibus metus.</p></div>
    <svg class="status" viewBox="0 0 24 24" fill="none" stroke="var(--ok)" stroke-width="1.6"><circle cx="12" cy="12" r="11"/><path d="M7 12l3.5 3.5L17 9"/></svg>
  </li>
  <li class="file-row">
    <div class="file-thumb" role="img" aria-label="Lumen TV app icon" style="background:radial-gradient(circle,#3a3f44 0 26%,#7fbfbe 28%)"></div>
    <div class="file-text"><h2 class="file-name">Lumen TV</h2><p class="file-desc">Lorem ipsum dolor sit amet, consectetur adipiscing elit. Aliquam ut dignissim dolor.<br>Pellentesque ex elit, interdum at ex nec, tincidunt faucibus metus.</p></div>
    <svg class="status" viewBox="0 0 24 24" fill="none" stroke="var(--bad)" stroke-width="1.6"><circle cx="12" cy="12" r="11"/><path d="M8 8l8 8M16 8l-8 8"/></svg>
  </li>
  <li class="file-row">
    <div class="file-thumb" role="img" aria-label="Nimbus TV app icon" style="background:radial-gradient(circle,#3b3556 0 35%,#1c3340 70%)"></div>
    <div class="file-text"><h2 class="file-name">Nimbus TV</h2><p class="file-desc">Lorem ipsum dolor sit amet, consectetur adipiscing elit. Aliquam ut dignissim dolor.<br>Pellentesque ex elit, interdum at ex nec, tincidunt faucibus metus.</p></div>
    <svg class="status" viewBox="0 0 24 24" fill="none" stroke="var(--ok)" stroke-width="1.6"><circle cx="12" cy="12" r="11"/><path d="M7 12l3.5 3.5L17 9"/></svg>
  </li>
  <li class="file-row">
    <div class="file-thumb" role="img" aria-label="Kernel Time app icon" style="background:radial-gradient(circle,#c23a3a 0 30%,#141414 60%)"></div>
    <div class="file-text"><h2 class="file-name">Kernel Time</h2><p class="file-desc">Lorem ipsum dolor sit amet, consectetur adipiscing elit. Aliquam ut dignissim dolor.<br>Pellentesque ex elit, interdum at ex nec, tincidunt faucibus metus.</p></div>
    <svg class="status" viewBox="0 0 24 24" fill="none" stroke="var(--ok)" stroke-width="1.6"><circle cx="12" cy="12" r="11"/><path d="M7 12l3.5 3.5L17 9"/></svg>
  </li>
</ul>

<footer class="site-footer">Copyright 2018 FILEHARBOR | All Rights Reserved</footer>
</body>
</html>
```